Company portfolio catalog

Our company - "The Velvet Nook" specializes in soft furnishings such as:
- curtains
- blinds
- wallpaper
- solar films
- re-upholstery

We also carry prestigious brands such as Marlow Pennick, Vextra motors and Orlena fabrics.

See our website - www.thevelvetnook-example.com.sg
our logo, showroom pic as attached

We want the feel to be a little fun and sleek as we're dealing with interior, but yet look expensive and classy....

Industry/Entity Type

Boutique

```html
<!DOCTYPE html>
<html lang="en">
<head>
<meta charset="utf-8">
<title>The Velvet Nook — Portfolio Catalogue</title>
<link rel="stylesheet" href="https://fonts.googleapis.com/css2?family=Questrial&family=Dancing+Script:wght@700&family=Roboto+Condensed:wght@400;700&family=Open+Sans:wght@400;600&display=swap">
<style>
  :root {
    --canvas: #e9e6e1;
    --cover-dark: #2b2a2a;
    --cover-band: #bfbfbf;
    --ink-light: #f2f2f2;
    --slate-top: #3a3f44;
    --slate-bottom: #5d646a;
    --page-white: #ffffff;
    --text-soft: #d8dde1;
    --shadow: rgba(0,0,0,0.18);
  }
  * { box-sizing: border-box; margin: 0; padding: 0; }
  html, body { width: 1200px; height: 899px; overflow: hidden; }
  body { background: var(--canvas); position: relative; }

  .cover, .spread { position: absolute; top: 210px; height: 480px; box-shadow: 0 6px 18px var(--shadow); }

  /* Cover */
  .cover { left: 75px; width: 340px; background: var(--page-white); overflow: hidden; }
  .cover__masthead { height: 230px; background: var(--cover-dark); text-align: center; padding-top: 118px; }
  .cover__name { font-family: "Questrial", sans-serif; font-size: 30px; color: var(--ink-light); font-weight: 400; letter-spacing: 0.2px; }
  .cover__tagline { font-family: "Dancing Script", cursive; font-size: 17px; color: var(--ink-light); margin-top: 12px; letter-spacing: 0.5px; }
  .cover__band { height: 14px; background: var(--cover-band); }
  .cover__rule { height: 3px; background: var(--page-white); }
  .cover__photo { height: 233px; background: linear-gradient(100deg, #4a4a4c 0%, #7b7b7d 35%, #c9c9c6 70%, #e4e3df 100%); }

  /* Spread */
  .spread { left: 445px; width: 680px; display: flex; }
  .page { width: 340px; height: 480px; position: relative; overflow: hidden; }
  .page--text { background: linear-gradient(180deg, var(--slate-top), var(--slate-bottom)); padding: 38px 30px 0 30px; color: var(--text-soft); font-family: "Open Sans", sans-serif; }
  .page__title { font-family: "Roboto Condensed", sans-serif; font-weight: 700; font-size: 34px; color: var(--page-white); letter-spacing: 1px; }
  .page__kicker { font-size: 7.5px; margin: 4px 0 12px; color: var(--page-white); }
  .page__body { font-size: 7.5px; line-height: 1.6; margin-bottom: 12px; }
  .page__subhead { font-size: 9px; font-weight: 600; color: var(--page-white); margin: 18px 0 6px; }

  .page--gallery { background: var(--page-white); }
  .gallery__hero { position: absolute; left: 0; top: 0; width: 340px; height: 290px; background: linear-gradient(160deg, #f3efe6 0%, #e3dccd 55%, #8d8983 100%); }
  .gallery__row { position: absolute; left: 0; top: 296px; width: 340px; height: 184px; display: flex; gap: 5px; }
  .gallery__tile { flex: 1; }
  .tile--sheer { background: linear-gradient(180deg, #c8d3d8, #98a8b0); }
  .tile--print { background: linear-gradient(180deg, #eeece8, #a6a4a0); }
  .tile--colour { background: linear-gradient(90deg, #e9822f, #f2d04a 35%, #8fc84e 60%, #e44f8c 100%); }
</style>
</head>
<body>
  <section class="cover">
    <header class="cover__masthead">
      <h1 class="cover__name">The Velvet Nook</h1>
      <p class="cover__tagline">Premium Soft Furnishings</p>
    </header>
    <div class="cover__band"></div>
    <div class="cover__rule"></div>
    <div class="cover__photo" role="img" aria-label="Showroom interior with grey curtains, roller blinds and a small table with chairs"></div>
  </section>

  <section class="spread">
    <article class="page page--text">
      <h2 class="page__title">CURTAINS</h2>
      <p class="page__kicker">Singapore: we offer you nothing but the best</p>
      <p class="page__body">In Singapore, the types of curtains are endless. There is a wide range of styles, colours and fabrics to choose from for every room. Our team will guide you from the first sketch to the final fitting, so each window feels tailored to the way you live.</p>
      <p class="page__body">Our curtain company offers a wide variety of curtain choices to fit any style and décor. Sheer panels soften daylight while lined drapes add warmth and privacy. Blackout curtains block outside light and noise, help keep rooms cool and protect furniture from fading. Every set is measured, sewn and hung by our own craftsmen for a clean finish.</p>
      <h3 class="page__subhead">Professional Benefits of Black-out Curtains</h3>
      <p class="page__body">Our black-out curtains are also used in hospitals between patients' beds and in studios by photographers who need full control of the light. With the right fabric, you can shape the mood of any room to suit your preferences.</p>
    </article>
    <article class="page page--gallery">
      <div class="gallery__hero" role="img" aria-label="Cream curtains with dark patterned tops beside a window seat with striped cushions"></div>
      <div class="gallery__row">
        <div class="gallery__tile tile--sheer" role="img" aria-label="Pale blue sheer curtains in a bright living room"></div>
        <div class="gallery__tile tile--print" role="img" aria-label="White curtains with black floral print"></div>
        <div class="gallery__tile tile--colour" role="img" aria-label="Bright multicoloured sheer curtains"></div>
      </div>
    </article>
  </section>
</body>
</html>
```